Ridgeline Outfitters Business Cards

Recently had a logo done with Artfolio and now looking for a business card to go along with it.

Target Market(s)

Ridgeline Outfitters is a weapons dealer. My market will be primarily men, hunting, shooting type.

Industry/Entity Type

Business

Contact Information for Business Card

I selected double sided, but this is not required, single or double is going to be fine. I picture the logo on one side, or perhaps just the circle which contains "RO" with the remaining info on the other side.

Font styles to use
Sans Serif

Requirements
Must have
• My name: Milo Brandt
• Title: Owner
• tel: 612-555-0187
• web: www.ridgelineoutfittersmn.example
Nice to have
• I like the concept of a black business card. I would like to keep the colors monotone, black, grey, white or red. Red is acceptable because it is in the logo. I have also seen cards that are matte black with shiny black as well, perhaps for the logo (or circle RO) part of the logo.
• I will upload a couple of the logos for use, and also an example I just found of the black on black. and some others that have a nice contrast.
Should not have
• lots of colors are not wanted.

```html
<!DOCTYPE html>
<html lang="en">
<head>
<meta charset="utf-8">
<title>Ridgeline Outfitters Business Cards</title>
<link rel="stylesheet" href="https://fonts.googleapis.com/css2?family=Courier+Prime:wght@400;700&display=swap">
<style>
  :root {
    --backdrop: #d9d6d1;
    --card-black: #050505;
    --panel-grey: #2b2b2b;
    --arc-grey: #5c5c5c;
    --arc-light: #7a7a7a;
    --brand-red: #e0232b;
    --text-white: #f4f4f4;
    --text-grey: #8a8a8a;
  }
  * { box-sizing: border-box; margin: 0; padding: 0; }
  html, body {
    width: 1200px; height: 924px; overflow: hidden;
    background: var(--backdrop);
    font-family: "Courier Prime", "Courier New", monospace;
  }
  .canvas { position: relative; width: 1200px; height: 924px; }
  .card {
    position: absolute;
    width: 520px; height: 297px;
    background: var(--card-black);
    border-radius: 4px;
    overflow: hidden;
    box-shadow: 0 10px 24px rgba(0,0,0,0.28);
  }
  .card-art { position: absolute; inset: 0; }

  /* Front */
  .card-front { left: 70px; top: 110px; }
  .front-brand {
    position: absolute; left: 0; right: 0; top: 118px;
    display: flex; align-items: center; justify-content: center; gap: 12px;
  }
  .brand-dot {
    width: 40px; height: 40px; border-radius: 50%;
    border: 5px solid var(--arc-grey);
    flex: none;
  }
  .brand-block { display: flex; flex-direction: column; align-items: center; }
  .brand-name {
    color: var(--brand-red);
    font-weight: 700; font-size: 20px; letter-spacing: 1px;
    text-transform: uppercase; white-space: nowrap;
  }
  .brand-rule {
    width: 100%; height: 2px; background: var(--arc-grey); margin: 4px 0 5px;
  }
  .brand-url { color: var(--text-grey); font-size: 8px; letter-spacing: 0.3px; white-space: nowrap; }

  /* Back */
  .card-back { left: 610px; top: 500px; }
  .person { position: absolute; left: 44px; top: 92px; }
  .person-name { color: var(--text-white); font-weight: 700; font-size: 30px; letter-spacing: 0.5px; }
  .person-title { color: var(--text-white); font-weight: 700; font-size: 17px; margin: 2px 0 0 14px; }
  .contact-list { position: absolute; left: 56px; top: 186px; list-style: none; }
  .contact-item {
    display: flex; align-items: center; gap: 10px;
    color: var(--text-white); font-size: 12px; height: 28px; white-space: nowrap;
  }
  .contact-item.phone { font-size: 17px; }
  .contact-icon { width: 24px; height: 22px; flex: none; }
</style>
</head>
<body>
<main class="canvas">

  <section class="card card-front" aria-label="Business card front">
    <svg class="card-art" width="520" height="297" viewBox="0 0 520 297" aria-hidden="true">
      <path d="M0 0 L30 0 Q130 148 30 297 L0 297 Z" fill="#141414"/>
      <path d="M30 0 Q130 148 30 297" fill="none" stroke="var(--arc-grey)" stroke-width="7"/>
      <path d="M520 0 L490 0 Q390 148 490 297 L520 297 Z" fill="#141414"/>
      <path d="M490 0 Q390 148 490 297" fill="none" stroke="var(--arc-grey)" stroke-width="7"/>
    </svg>
    <div class="front-brand">
      <span class="brand-dot"></span>
      <div class="brand-block">
        <span class="brand-name">Ridgeline Outfitters</span>
        <span class="brand-rule"></span>
        <span class="brand-url">www.ridgelineoutfittersmn.example</span>
      </div>
    </div>
  </section>

  <section class="card card-back" aria-label="Business card back">
    <svg class="card-art" width="520" height="297" viewBox="0 0 520 297" aria-hidden="true">
      <circle cx="600" cy="130" r="235" fill="var(--panel-grey)" stroke="var(--arc-light)" stroke-width="6"/>
      <circle cx="450" cy="130" r="72" fill="none" stroke="var(--arc-grey)" stroke-width="10"/>
    </svg>
    <div class="person">
      <p class="person-name">Milo Brandt</p>
      <p class="person-title">Owner</p>
    </div>
    <ul class="contact-list">
      <li class="contact-item phone">
        <svg class="contact-icon" viewBox="0 0 24 22" aria-hidden="true">
          <path d="M2 8 Q12 0 22 8 L19 11 L16 8 L16 6 Q12 4 8 6 L8 8 L5 11 Z" fill="var(--text-white)"/>
          <rect x="5" y="11" width="14" height="9" rx="2" fill="var(--text-white)"/>
          <circle cx="12" cy="15.5" r="2.5" fill="var(--card-black)"/>
        </svg>
        <span>612-555-0187</span>
      </li>
      <li class="contact-item">
        <svg class="contact-icon" viewBox="0 0 24 22" aria-hidden="true">
          <rect x="1" y="4" width="22" height="15" fill="var(--text-white)"/>
          <path d="M1 4 L12 13 L23 4" fill="none" stroke="var(--card-black)" stroke-width="2"/>
        </svg>
        <span>info@ridgelineoutfittersmn.example</span>
      </li>
      <li class="contact-item">
        <svg class="contact-icon" viewBox="0 0 24 22" aria-hidden="true">
          <g fill="none" stroke="var(--text-white)" stroke-width="1.4">
            <circle cx="12" cy="11" r="9.5"/>
            <ellipse cx="12" cy="11" rx="4.5" ry="9.5"/>
            <line x1="12" y1="1.5" x2="12" y2="20.5"/>
            <line x1="2.5" y1="11" x2="21.5" y2="11"/>
            <line x1="4" y1="6" x2="20" y2="6"/>
            <line x1="4" y1="16" x2="20" y2="16"/>
          </g>
        </svg>
        <span>www.ridgelineoutfittersmn.example</span>
      </li>
    </ul>
  </section>

</main>
</body>
</html>
```